Bubble map/flip book

I need someone to create a bubble map with explanations using the attached. This will be used to create a color coded flip book/manual. I need you to clean this up.

Dorothywinslade@postlark.com

```html
<!DOCTYPE html>
<html lang="en">
<head>
<meta charset="utf-8">
<title>Coding Denials</title>
<link rel="stylesheet" href="https://fonts.googleapis.com/css2?family=Arimo:wght@400;700&family=Open+Sans:ital@1&display=swap">
<style>
  :root {
    --header-blue: #0f69b4;
    --tag-red: #ee3338;
    --tag-orange: #f58634;
    --tag-green: #8cc63f;
    --ink: #333333;
    --letter-grey: #d9d9d9;
    --footer-grey: #9ea3a6;
    --footer-ink: #555b60;
    --paper: #ffffff;
  }
  * { margin: 0; padding: 0; box-sizing: border-box; }
  html, body { width: 927px; height: 1200px; overflow: hidden; background: var(--paper); }
  body { position: relative; font-family: "Arimo", Arial, sans-serif; color: var(--ink); }

  .page-header {
    position: absolute; left: 0; top: 0; width: 927px; height: 328px;
    background: var(--header-blue);
  }
  .page-title {
    position: absolute; left: 123px; top: 228px;
    font-size: 54px; font-weight: 700; color: #fff;
    text-shadow: 3px 4px 5px rgba(0,0,0,0.55);
    letter-spacing: 0.3px;
  }

  .tag {
    position: absolute; left: 125px; height: 28px;
    color: #fff; font-weight: 700; font-size: 21px;
    padding: 2px 16px 0; border-radius: 4px; line-height: 24px;
    white-space: nowrap;
  }
  .tag-example { top: 399px; width: 140px; background: var(--tag-red); }
  .tag-account { top: 518px; width: 292px; background: var(--tag-orange); }
  .tag-verify  { top: 1041px; width: 597px; background: var(--tag-green); }

  .rail { position: absolute; left: 144px; width: 1px; }
  .rail-example { top: 427px; height: 31px; background: var(--tag-red); }
  .rail-account { top: 547px; height: 443px; background: var(--tag-orange); }

  .dot { position: absolute; left: 140px; width: 9px; height: 9px; border-radius: 50%; }
  .dot-red { background: var(--tag-red); }
  .dot-orange { background: var(--tag-orange); }

  .example-text {
    position: absolute; left: 164px; top: 448px; width: 680px;
    font-size: 18.2px; line-height: 21px;
  }
  .note-item { position: absolute; left: 164px; font-size: 18px; white-space: nowrap; }

  .reason { position: absolute; left: 172px; height: 32px; }
  .reason-letter {
    position: absolute; left: 0; top: -6px; width: 24px; text-align: center;
    font-size: 32px; font-weight: 700; color: var(--letter-grey);
  }
  .reason-text { position: absolute; left: 35px; top: 4px; font-size: 15.2px; white-space: nowrap; }

  .page-footer-url {
    position: absolute; right: 55px; top: 1143px;
    font-family: "Open Sans", Arial, sans-serif; font-style: italic;
    font-size: 15px; color: var(--footer-ink);
  }
  .page-number {
    position: absolute; left: 894px; top: 1137px; width: 33px; height: 33px;
    background: var(--footer-grey); color: #fff; font-size: 25px;
    text-align: center; line-height: 34px;
  }
</style>
</head>
<body>
  <header class="page-header">
    <h1 class="page-title">Coding Denials</h1>
  </header>

  <div class="tag tag-example">Example:</div>
  <div class="rail rail-example"></div>
  <span class="dot dot-red" style="top:454px"></span>
  <p class="example-text">Claim denied as procedure code used 99203 is for a new patient and this is an established patient.</p>

  <div class="tag tag-account">Account note will include:</div>
  <div class="rail rail-account"></div>

  <span class="dot dot-orange" style="top:559px"></span>
  <p class="note-item" style="top:553px">How information was obtained</p>
  <span class="dot dot-orange" style="top:584px"></span>
  <p class="note-item" style="top:579px">Name a representative</p>
  <span class="dot dot-orange" style="top:610px"></span>
  <p class="note-item" style="top:605px">Claim number</p>
  <span class="dot dot-orange" style="top:636px"></span>
  <p class="note-item" style="top:631px">Denial date</p>
  <span class="dot dot-orange" style="top:662px"></span>
  <p class="note-item" style="top:657px">What was denied: CPT, HCPCS, modifier,diagnosis?</p>
  <span class="dot dot-orange" style="top:688px"></span>
  <p class="note-item" style="top:683px">What code denied?</p>
  <span class="dot dot-orange" style="top:720px"></span>
  <p class="note-item" style="top:709px">Why was it denied?</p>

  <div class="reason" style="top:752px"><span class="reason-letter">A</span><span class="reason-text">Not covered?</span></div>
  <div class="reason" style="top:790px"><span class="reason-letter">B</span><span class="reason-text">Bundled to another code on the claim? Which code is it bundled with?</span></div>
  <div class="reason" style="top:827px"><span class="reason-letter">C</span><span class="reason-text">Not a covered benefit per patient policy? Why ? What is the service?</span></div>
  <div class="reason" style="top:865px"><span class="reason-letter">D</span><span class="reason-text">Invalid modifier? What modifier was billed ? What is needed?</span></div>
  <div class="reason" style="top:902px"><span class="reason-letter">E</span><span class="reason-text">Diagnosis does not match CPT? Verify codes billed do not relate to each other.</span></div>

  <span class="dot dot-orange" style="top:960px"></span>
  <p class="note-item" style="top:951px">Appeal address</p>
  <span class="dot dot-orange" style="top:986px"></span>
  <p class="note-item" style="top:982px">Timely filing</p>

  <div class="tag tag-verify">Verify that the claim was billed with the CPT code stated.</div>

  <p class="page-footer-url">www.example.com</p>
  <div class="page-number">5</div>
</body>
</html>
```